Business Card Design Project

Hello
I want a Simple Business card that uses the company logo that is easily reasonable but looks professional as I am an IT Services company and would look to share these cards with prospective clients.
The details are:
Kestrel Arc Solutions
14 Morrow Lane
Birmingham
B7 4QX
Telephone 0845 217 6640
I would like my name Oliver Hastings and my title Director on the card.
Target Market(s)
IT Professionals
Industry/Entity Type
Business

```html
<!DOCTYPE html>
<html lang="en">
<head>
<meta charset="utf-8">
<title>Kestrel Arc Solutions – Business Cards</title>
<link href="https://fonts.googleapis.com/css2?family=Lato:wght@400;700&display=swap" rel="stylesheet">
<style>
  :root {
    --backdrop: #d9d9d9;
    --card: #f7f7f5;
    --ink: #1b1b1b;
    --ink-soft: #2a2a2a;
    --mark: #7cbf45;
    --band-1: #5fb646;
    --band-2: #79bf45;
    --band-3: #8cc95a;
    --band-4: #a5cf4a;
    --band-5: #d3df4c;
    --band-6: #f0c94e;
  }
  * { margin: 0; padding: 0; box-sizing: border-box; }
  html, body {
    width: 1200px; height: 900px; overflow: hidden;
    background: var(--backdrop);
    font-family: "Lato", sans-serif;
    color: var(--ink);
  }
  .sheet {
    position: relative; width: 1200px; height: 900px;
  }
  .card {
    position: absolute; width: 560px; height: 320px;
    background: var(--card);
    box-shadow: 0 2px 6px rgba(0,0,0,0.12);
    overflow: hidden;
  }
  .card--front { left: 320px; top: 100px; }
  .card--back  { left: 320px; top: 480px; }

  /* brand name set in text font */
  .brand { display: flex; align-items: center; gap: 12px; }
  .brand__dot { width: 26px; height: 26px; border-radius: 50%; background: var(--mark); flex: none; }
  .brand__name { font-weight: 700; color: var(--ink); line-height: 1.1; }

  /* colour band */
  .band { position: absolute; display: flex; flex-direction: column; }
  .band span { flex: 1; }
  .band span:nth-child(1) { background: var(--band-1); }
  .band span:nth-child(2) { background: var(--band-2); }
  .band span:nth-child(3) { background: var(--band-3); }
  .band span:nth-child(4) { background: var(--band-4); }
  .band span:nth-child(5) { background: var(--band-5); }
  .band span:nth-child(6) { background: var(--band-6); }

  /* front card */
  .card--front .brand { position: absolute; left: 0; right: 22px; top: 56px; justify-content: center; }
  .card--front .brand__name { font-size: 30px; }
  .card--front .band { right: 0; top: 0; bottom: 0; width: 22px; }
  .front__phone { position: absolute; left: 40px; top: 140px; width: 160px; text-align: center; font-size: 15px; }
  .front__person { position: absolute; left: 180px; top: 146px; width: 200px; text-align: center; }
  .front__address { position: absolute; right: 56px; top: 196px; width: 170px; text-align: center; font-size: 15px; line-height: 1.35; }
  .icon { display: block; margin: 0 auto 10px; width: 30px; height: 30px; }
  .person__name { font-weight: 700; font-size: 19px; }
  .person__title { font-size: 14px; color: var(--ink-soft); margin-top: 2px; }

  /* back card */
  .card--back .brand { position: absolute; left: 40px; top: 132px; width: 250px; }
  .card--back .brand__name { font-size: 27px; }
  .card--back .band { left: 298px; top: 36px; bottom: 36px; width: 14px; }
  .back__details { position: absolute; left: 322px; right: 20px; top: 104px; text-align: center; line-height: 1.35; }
  .back__details .person__name { font-size: 20px; }
  .back__details .person__title { font-size: 15px; }
  .back__phone { margin-top: 14px; font-size: 15px; }
  .back__address { margin-top: 8px; font-size: 15px; }
</style>
</head>
<body>
<main class="sheet">

  <section class="card card--front" aria-label="Business card front">
    <div class="brand">
      <span class="brand__dot"></span>
      <span class="brand__name">Kestrel Arc Solutions</span>
    </div>

    <div class="front__phone">
      <svg class="icon" viewBox="0 0 30 30" aria-hidden="true">
        <circle cx="15" cy="15" r="13.5" fill="none" stroke="#1b1b1b" stroke-width="2"/>
        <path d="M9 12.5c0-2 2.6-3 6-3s6 1 6 3l-1.8 1.2-1.6-1.4v-1.1h-5.2v1.1l-1.6 1.4z" fill="#1b1b1b"/>
        <rect x="10" y="14.5" width="10" height="6" rx="1.2" fill="#1b1b1b"/>
      </svg>
      0845 217 6640
    </div>

    <div class="front__person">
      <div class="person__name">Oliver Hastings</div>
      <div class="person__title">Director</div>
    </div>

    <div class="front__address">
      <svg class="icon" viewBox="0 0 30 30" aria-hidden="true">
        <circle cx="15" cy="15" r="13.5" fill="none" stroke="#1b1b1b" stroke-width="2"/>
        <path d="M15 7.5a5 5 0 0 0-5 5c0 3.8 5 9.5 5 9.5s5-5.7 5-9.5a5 5 0 0 0-5-5z" fill="#1b1b1b"/>
        <circle cx="15" cy="12.5" r="1.9" fill="#f7f7f5"/>
      </svg>
      14 Morrow Lane<br>Birmingham, B7 4QX
    </div>

    <div class="band" aria-hidden="true"><span></span><span></span><span></span><span></span><span></span><span></span></div>
  </section>

  <section class="card card--back" aria-label="Business card back">
    <div class="brand">
      <span class="brand__dot"></span>
      <span class="brand__name">Kestrel Arc Solutions</span>
    </div>

    <div class="band" aria-hidden="true"><span></span><span></span><span></span><span></span><span></span><span></span></div>

    <div class="back__details">
      <div class="person__name">Oliver Hastings</div>
      <div class="person__title">Director</div>
      <div class="back__phone">0845 217 6640</div>
      <div class="back__address">14 Morrow Lane<br>Birmingham, B7 4QX</div>
    </div>
  </section>

</main>
</body>
</html>
```